Business Card for a finance professional

I need a business card design to introduce myself to a professional networking (mainly banks) and potential companies to hire and remember me. I would like to use black, grey, white and maybe gold/silver colors and maybe something with my initials(R L F P T). The final design should communicate seriousness, profissionalism and something innovative.

The basic informations in the card are: Name, e-mail, phone number and trabnet. (I'm thinking to put some directly short link to my trabnet account or maybe some app - non QR Code - to add my contacts to a phone directly.)

My name is Mariana Lopes Ferreira Pinto dos Reis (I prefer to use only 'Mariana Lopes' or 'Mariana Reis' but i'm open to other suggestions) and I have 26 years old (just if it helps to build based in my age).
Updates

Dear designers, I wish to thank your participation in this project! It was very difficult to choose one! Thank your for your work! Best regards and success. Mariana

Target Market(s)

Potential hires and big companies.

Industry/Entity Type

Finance

Requirements
Must have
• The informations required at the business card are:
Name: Mariana Lopes F. P. dos Reis
Email: mariana.lop.reis@quellomail.com
Phone: +55 61 8493 5710
TrabNet: http://br.trabnet-perfis.com/in/marianalr/
Nice to have
• Modern and innovative look.
I suggest to use the colors black, grey, white, gold and/or silver, but I'm open to other colors.
Should not have
• A message showing that I need to be hired. It's more to "know me and remember me" than "hire me please".

```html
<!DOCTYPE html>
<html lang="en">
<head>
<meta charset="utf-8">
<title>Mariana Lopes — Business Card</title>
<link rel="stylesheet" href="https://fonts.googleapis.com/css2?family=Ruluko&family=Raleway:wght@400;700&display=swap">
<style>
  :root {
    --bg: #d9d9d9;
    --band: #f3f3f2;
    --wine-light: #a01c48;
    --wine-mid: #861f3d;
    --wine-dark: #701831;
    --name-front: #7a1a33;
    --ink: #4a3a2c;
    --ink-soft: #5a4a3c;
  }
  html, body {
    margin: 0;
    width: 1200px;
    height: 1000px;
    overflow: hidden;
    background: var(--bg);
  }
  .canvas {
    position: relative;
    width: 1200px;
    height: 1000px;
  }
  .card {
    position: absolute;
    top: 150px;
    width: 420px;
    height: 700px;
    overflow: hidden;
    box-shadow: 0 8px 22px rgba(0,0,0,0.22);
    background: var(--wine-mid);
  }
  .card--front { left: 140px; }
  .card--back  { left: 640px; }
  .card-pattern {
    position: absolute;
    left: 0;
    right: 0;
    top: 0;
    bottom: 0;
    background: linear-gradient(100deg, var(--wine-light) 0%, var(--wine-mid) 50%, var(--wine-dark) 100%);
  }
  .band {
    position: absolute;
    left: 0;
    right: 0;
    background: var(--band);
    display: flex;
    flex-direction: column;
    justify-content: center;
    align-items: center;
    text-align: center;
  }
  .card--front .band {
    top: 140px;
    height: 150px;
  }
  .front-name {
    margin: 0;
    font-family: "Ruluko", sans-serif;
    font-weight: 400;
    font-size: 54px;
    color: var(--name-front);
    letter-spacing: 0.5px;
    white-space: nowrap;
  }
  .card--back .band {
    top: 170px;
    height: 170px;
  }
  .back-name {
    margin: 0 0 8px;
    font-family: "Raleway", sans-serif;
    font-weight: 700;
    font-size: 19px;
    line-height: 1.25;
    color: var(--ink);
  }
  .contact {
    margin: 0;
    padding: 0;
    list-style: none;
    font-family: "Raleway", sans-serif;
    font-size: 13.5px;
    line-height: 1.5;
    color: var(--ink-soft);
    white-space: nowrap;
  }
</style>
</head>
<body>
  <main class="canvas">
    <section class="card card--front" aria-label="Card front">
      <div class="card-pattern" role="img" aria-label="Vertical stripe pattern in wine and magenta tones"></div>
      <div class="band">
        <h1 class="front-name">Mariana Lopes</h1>
      </div>
    </section>

    <section class="card card--back" aria-label="Card back">
      <div class="card-pattern" role="img" aria-label="Vertical stripe pattern in wine and magenta tones"></div>
      <div class="band">
        <h2 class="back-name">Mariana Lopes<br>F. P. dos Reis</h2>
        <ul class="contact">
          <li>Phone: +55 61 8493 5710</li>
          <li>Email: mariana.lop.reis@quellomail.com</li>
          <li>TrabNet: http://br.trabnet-perfis.com/in/marianalr/</li>
        </ul>
      </div>
    </section>
  </main>
</body>
</html>
```